website for local kavenda practicioner and yoga teacher trainer

The website should function primarily as:
A place where people can discover Kavenda and book sessions.
A central hub connecting all of my work.
A professional home that reflects my personality and approach.
Website design for Liesbet Oonwerk — Kavenda® Structural Integration practitioner, movement educator, yoga teacher and teacher trainer.
A website that can grow with future projects.
The website should feel: Warm, Human, Invitational, Professional, Accessible, Intelligent, Calm, Clear, Playful, Exploratory, Trustworthy
Avoid: New age aesthetics, Mystical clichés, Excessive spirituality, ”Guru" vibes, Overly clinical design, Corporate wellness branding, Busy layouts
Think: modern, grounded, curious and real.
My work combines three interconnected areas:
1.Bodywork: Touch, structure, awareness and one-on-one support.
2. Movement: Yoga, Pilates and embodied movement.
3. Education: Teacher trainings, workshops and continued learning.
Underlying values:
Curiosity over certainty
Possibility over perfection
Complexity without overwhelm
Science and lived experience together
Exploration rather than dogma
Human beings before methods
The primary goal of the website is to introduce people to Kavenda® Structural Integration and make it easy for them to:
Understand what Kavenda is
Discover whether it might be relevant for them
Learn what to expect from a session
Book an appointment
Booking should always feel visible and easy.
Secondary Goal: Present all other aspects of my work in one coherent place:
Yoga classes
Pilates classes
Teacher trainings
Workshops
Retreats
One-on-one movement sessions
Collaborations with studios
Website Structure
1: HOME
1.1.Hero Section: Large welcoming image
1.2 Two Main Pathways
- Bodywork: Kavenda® Structural Integration
- Movement & Education: Yoga, Pilates, trainings, workshops and retreats
- About Preview: Small introduction with portrait. + Button:
Read More
1.3 Current Events / What's Coming Up: Upcoming trainings, workshops and retreats. (This section should be easy to update)
1.4. Contact / Newsletter: Simple contact information
2: Kavenda® Structural Integration
What is Kavenda?
For whom is it?
What does a session look like?
FAQ
Prices
Booking
Future possibility:
Kaven Movement sessions
3: Movement
- Introductory text.
- Studio Classes (link to “my home base” - > local yoga studio)
- One-to-One Sessions: booking option (this is small; not a key aspect I want to promote)
- Workshops/ Retreats / Teacher Trainings => This section should be flexible and easy to update. Visitors should be able to click into specific offerings.
4. Events
Dynamic page for: Teacher trainings, Retreats, Workshops (see section in movement; here more elaborate)
Each event should contain: Image, Short description, Location, Date, Button for more information. (Linking to hosting studio/location)
5. Work With Me
For studios, organisations and teacher training schools.
Examples: Guest teaching, Workshops, Anatomy, Sequencing, Teacher development , Continuing education -> Clear call-to-action.
Call to action!!=> Book a Session
Prominent button in the navigation.
Footer:
- About Me: Longer biography (6th page)
Personal story and background.
- Testimonials (7th page): Separate page containing testimonials from:
Kavenda clients
Students
Teacher trainees
- Contact: 8th page
Visual Direction
Natural textures. Lots of white space.Editorial feeling.Professional photography.Simple navigation.
Less "wellness influencer.” More:Thoughtful, Contemporary, Timeless, Grounded, Human
Photography should show:
Teaching
Hands-on work
Natural movement
Real interaction
Simplicity
Avoid stereotypical yoga imagery and overly spiritual aesthetics.
Keywords
Warm. Curious. Human. Professional. Embodied. Intelligent. Accessible. Playful. Grounded. Exploratory. Real.
Inspiration / Core Message
Helping people feel more at home in their bodies through touch, movement and education.
The website should communicate that these are not separate services, but different expressions of the same intention:
Bodywork • Movement • Education.
Colours:
light orange/beige: e3d5c4
light orange/off white: f9f7f3
gray azure: 556b78
orange: d07b5a
grey orange: c09f80
dark grey: 3e3e3e
dark gray cyan 2f4f4f
gray green colour: a7c4a0
Fonts: Montserrat and Poppins + raleway
In added documents a try out idea of a website + logo. I will mainly use the logo with diffrent colours (image next to text).
My audience consists of people who want to feel more at home in their bodies and who appreciate a thoughtful, grounded and human approach to movement, touch and education. (30-65yo)
wellbeing
5+ page
- montserrat, poppins, raleway

```html
<!DOCTYPE html>
<html lang="en">
<head>
<meta charset="utf-8">
<title>Liesbet Oonwerk — website pages</title>
<link href="https://fonts.googleapis.com/css2?family=Raleway:wght@300;400;500&family=Montserrat:wght@400;500;600;700&family=Poppins:wght@400;500&display=swap" rel="stylesheet">
<style>
:root{
  --beige:#e3d5c4;
  --offwhite:#f9f7f3;
  --azure:#556b78;
  --orange:#d07b5a;
  --greyorange:#c09f80;
  --darkgrey:#3e3e3e;
  --teal:#2f4f4f;
  --green:#a7c4a0;
  --line:#e4dbcf;
  --text:#3e3e3e;
  --muted:#6d6a66;
}
*{box-sizing:border-box;margin:0;padding:0}
html,body{width:1200px;height:4033px;overflow:hidden;background:#ffffff}
body{font-family:"Montserrat",sans-serif;color:var(--text);position:relative}
.column{position:absolute;top:0;width:575px;display:flex;flex-direction:column}
.column--left{left:23px}
.column--right{left:598px;box-shadow:-6px 0 14px rgba(0,0,0,.12)}
section,header,footer{position:relative;flex:none;overflow:hidden}

/* nav */
.site-nav{height:23px;background:var(--offwhite);display:flex;align-items:center;padding:0 62px 0 70px;border-bottom:1px solid var(--line)}
.brand{font-family:"Raleway",sans-serif;font-weight:500;font-size:7px;color:var(--darkgrey);display:flex;align-items:center;gap:4px}
.brand-dot{width:5px;height:5px;border-radius:50%;background:var(--azure)}
.nav-links{margin-left:auto;display:flex;gap:7px;font-size:4.2px;font-weight:600;letter-spacing:.3px;color:var(--muted)}
.nav-book{margin-left:8px;background:var(--orange);color:#fff;font-size:4.2px;font-weight:700;padding:3px 6px;letter-spacing:.3px}

/* type */
.eyebrow{font-size:4.2px;font-weight:700;letter-spacing:.5px;text-transform:uppercase;color:var(--orange);margin-bottom:5px}
.display{font-family:"Raleway",sans-serif;font-weight:400;font-size:30px;line-height:32px;color:var(--darkgrey);letter-spacing:-.2px}
.title{font-family:"Raleway",sans-serif;font-weight:400;font-size:18px;line-height:19px;color:var(--darkgrey)}
.title--light{color:#fff}
.body{font-size:5.2px;line-height:8px;color:var(--muted)}
.body--light{color:#d9e2df}
.btn-row{display:flex;gap:5px;margin-top:10px}
.btn{display:inline-block;background:var(--orange);color:#fff;font-size:4.2px;font-weight:700;letter-spacing:.4px;padding:4px 8px;text-transform:uppercase}
.btn--outline{background:#fff;color:var(--darkgrey);border:1px solid #cfc5b9}
.btn--teal{background:var(--teal)}
.btn--wide{display:block;text-align:center;padding:5px 0}

/* photo fills */
.photo{position:absolute}
.ph-warm{background:linear-gradient(160deg,#d8c9b8,#b39c86 55%,#c9a08f 85%,#d38aa0)}
.ph-portrait{background:linear-gradient(150deg,#6a5140,#8c6e58 45%,#3d3732)}
.ph-hands{background:linear-gradient(135deg,#e6d2c2,#c7a48d 60%,#e0cbbb)}
.ph-beach{background:linear-gradient(180deg,#b9b9b7,#a6a39c 55%,#8d8479)}
.ph-sunset{background:linear-gradient(180deg,#9c8c63,#c99b55 45%,#5b4a34)}
.ph-mono{background:linear-gradient(160deg,#3a3a3a,#8c8c8c 55%,#2a2a2a)}
.ph-mono2{background:linear-gradient(120deg,#cfcfcf,#6d6d6d 55%,#2f2f2f)}
.ph-dusk{background:linear-gradient(180deg,#7c5a43,#b8784e 50%,#3f2e24)}
.ph-studio{background:linear-gradient(180deg,#9a8a86,#7a6d73 55%,#c7b3a8)}

/* bands */
.band--beige{background:var(--beige)}
.band--white{background:var(--offwhite)}
.band--teal{background:var(--teal)}

/* cards */
.card-grid{display:grid;grid-template-columns:repeat(3,140px);gap:7px}
.info-card{background:#fff;padding:8px 7px;border:1px solid var(--line)}
.info-card h3{font-family:"Raleway",sans-serif;font-weight:500;font-size:8.5px;line-height:10px;color:var(--darkgrey);margin-bottom:4px}
.event-card{background:#fff;border:1px solid var(--line);display:flex;flex-direction:column}
.event-card .ph{height:103px;position:relative}
.event-body{padding:7px 6px 6px;display:flex;flex-direction:column;flex:1}
.event-meta{font-size:3.6px;font-weight:700;color:var(--orange);letter-spacing:.3px;text-transform:uppercase;margin-bottom:3px}
.event-body h3{font-family:"Raleway",sans-serif;font-weight:500;font-size:8.5px;line-height:10px;color:var(--darkgrey);margin-bottom:4px}
.event-body .btn{margin-top:auto;text-align:center}

/* footer */
.site-footer{background:var(--darkgrey);padding:14px 62px 0 70px;display:grid;grid-template-columns:167px 140px 1fr}
.footer-brand{display:inline-block;background:var(--teal);color:#fff;font-family:"Raleway",sans-serif;font-weight:500;font-size:7px;padding:4px 8px;margin-bottom:5px}
.site-footer .body{color:#bdbab4;width:145px}
.footer-col h4{font-size:4.5px;font-weight:700;color:#fff;margin-bottom:4px}
.footer-col li{list-style:none;font-size:4.5px;line-height:8px;color:#bdbab4}

/* forms */
.form-card{position:absolute;background:#fff;border:1px solid var(--line);padding:10px 9px}
.field{margin-bottom:8px}
.field label{display:block;font-size:3.8px;font-weight:700;letter-spacing:.3px;color:var(--darkgrey);text-transform:uppercase;margin-bottom:3px}
.field .input{height:12px;border:1px solid #d6cec4;font-size:4.5px;color:var(--muted);padding:3px 4px}
.field .input--area{height:48px}
.field .input--select{display:flex;justify-content:space-between}

.list-rows li{list-style:none;font-size:5px;color:var(--muted);padding:6px 0;border-bottom:1px solid var(--line)}
</style>
</head>
<body>

<!-- ================= LEFT COLUMN ================= -->
<div class="column column--left">

  <!-- HOME -->
  <header class="site-nav">
    <div class="brand"><span class="brand-dot"></span>Liesbet Oonwerk</div>
    <nav class="nav-links"><span>KAVENDA</span><span>MOVEMENT</span><span>EVENTS</span><span>WORK WITH ME</span><span>ABOUT</span><span>TESTIMONIALS</span><span>CONTACT</span></nav>
    <span class="nav-book">BOOK A SESSION</span>
  </header>

  <section class="band--white" style="height:531px">
    <div style="position:absolute;left:55px;top:31px;width:210px">
      <p class="eyebrow">Kavenda structural integration · movement education</p>
      <h1 class="display">Bodywork<br>and<br>movement for<br>people who<br>want more<br>ease, support,<br>and choice.</h1>
      <p class="body" style="margin-top:8px;width:185px">Liesbet Oonwerk offers Kavenda Structural Integration, Kaven Movement sessions, yoga, Pilates, teacher education, workshops, and retreats with a calm, grounded approach.</p>
      <div class="btn-row"><span class="btn">Book a session</span><span class="btn btn--outline">See events</span></div>
    </div>
    <div style="position:absolute;left:55px;top:363px;display:flex;gap:5px">
      <div style="width:94px;height:122px;background:var(--beige);padding:8px 6px">
        <p class="eyebrow">Bodywork</p>
        <h3 class="info-title" style="font-family:Raleway,sans-serif;font-size:8px;line-height:9.5px;font-weight:500;margin-bottom:5px">Kavenda® Structural Integration</h3>
        <p class="body" style="font-size:4.5px;line-height:7px">Hands-on sessions that work with fascia, posture, breath, coordination, and your sense of support.</p>
      </div>
      <div style="width:100px;height:122px;background:var(--green);padding:8px 6px">
        <p class="eyebrow">Movement &amp; education</p>
        <h3 style="font-family:Raleway,sans-serif;font-size:8px;line-height:9.5px;font-weight:500;margin-bottom:5px">Yoga, Pilates, workshops, trainings</h3>
        <p class="body" style="font-size:4.5px;line-height:7px;color:#4a5a48">Movement learning for students, teachers, studios, and organisations who value clarity and curiosity.</p>
      </div>
    </div>
    <div class="photo ph-warm" role="img" aria-label="Woman in a plank position on a pink mat in a bright studio" style="left:273px;top:8px;width:245px;height:500px"></div>
  </section>

  <section class="band--beige" style="height:255px">
    <div class="photo ph-portrait" role="img" aria-label="Portrait of the practitioner outdoors" style="left:70px;top:30px;width:188px;height:195px"></div>
    <div style="position:absolute;left:277px;top:55px;width:230px">
      <p class="eyebrow">About Liesbet</p>
      <h2 class="title" style="font-size:19px;line-height:20px">A precise, human way of working with bodies.</h2>
      <p class="body" style="margin-top:7px">Liesbet brings together structural bodywork and movement teaching. Her sessions are attentive, collaborative, and practical, a place to listen to the body, understand patterns, and build more supportive ways of moving.</p>
      <p class="body" style="margin-top:4px">Her teaching is informed by Kavenda, yoga, Pilates, anatomy, and years of learning with people in real bodies, real schedules, and real lives.</p>
      <div class="btn-row"><span class="btn btn--outline">Read more</span></div>
    </div>
  </section>

  <section class="band--white" style="height:305px;padding:34px 0 0 70px">
    <p class="eyebrow">Upcoming</p>
    <h2 class="title" style="font-size:17px;margin-bottom:10px">Classes, workshops, trainings, retreats.</h2>
    <div class="card-grid">
      <article class="event-card"><div class="ph ph-mono" role="img" aria-label="Person folding forward on the floor in black and white"></div><div class="event-body"><p class="event-meta">21–22 September · Antwerp, Belgium</p><h3>Kavenda and Natural Movement Weekend</h3><p class="body">A small-group immersion exploring support, breath, walking, and the felt sense of uprightness.</p><span class="btn btn--outline">Learn more</span></div></article>
      <article class="event-card"><div class="ph ph-mono2" role="img" aria-label="Person in a downward dog on a mat in black and white"></div><div class="event-body"><p class="event-meta">18 October 2025 · Studio guest training</p><h3>Anatomy for Yoga Teachers</h3><p class="body">Practical anatomy and sequencing for teachers who want clearer cueing and more responsive classes.</p><span class="btn btn--outline">Learn more</span></div></article>
      <article class="event-card"><div class="ph ph-sunset" role="img" aria-label="Figure stretching in warm evening light"></div><div class="event-body"><p class="event-meta">6–9 February 2026 · Ardennes, Belgium</p><h3>Winter Retreat: Structure and Ease</h3><p class="body">Movement, rest, hands-on exploration, and quiet study in a relaxed format with generous space.</p><span class="btn btn--outline">Learn more</span></div></article>
    </div>
  </section>

  <section class="band--teal" style="height:167px">
    <div style="position:absolute;left:70px;top:30px;width:200px">
      <p class="eyebrow">Stay in touch</p>
      <h2 class="title title--light" style="font-size:17px">Notes on movement, anatomy, and upcoming dates.</h2>
      <p class="body body--light" style="margin-top:6px">Receive occasional updates about classes, workshops, retreats, and thoughtful resources for body awareness.</p>
    </div>
    <div style="position:absolute;left:277px;top:72px;display:flex;align-items:center;gap:10px">
      <div style="width:161px;height:13px;background:#fff;font-size:4.5px;color:#999;padding:4px 4px">you@example.com</div>
      <span style="font-size:4.2px;font-weight:700;color:#fff;letter-spacing:.3px">JOIN NEWSLETTER</span>
    </div>
  </section>

  <footer class="site-footer" style="height:94px">
    <div><span class="footer-brand">Liesbet Oonwerk</span><p class="body">Kavenda® Structural Integration, movement education, yoga, Pilates, trainings, workshops, and retreats.</p></div>
    <div class="footer-col"><h4>Explore</h4><ul><li>Kavenda Structural Integration</li><li>Movement</li><li>Events</li><li>Work with me</li></ul></div>
    <div class="footer-col"><h4>Connect</h4><ul><li>About</li><li>Testimonials</li><li>Contact</li></ul></div>
  </footer>

  <!-- MOVEMENT -->
  <header class="site-nav">
    <div class="brand"><span class="brand-dot"></span>Liesbet Oonwerk</div>
    <nav class="nav-links"><span>KAVENDA</span><span>MOVEMENT</span><span>EVENTS</span><span>WORK WITH ME</span><span>ABOUT</span><span>TESTIMONIALS</span><span>CONTACT</span></nav>
    <span class="nav-book">BOOK A SESSION</span>
  </header>

  <section class="band--white" style="height:294px">
    <div style="position:absolute;left:55px;top:31px;width:215px">
      <p class="eyebrow">Movement &amp; education</p>
      <h1 class="display">Yoga, Pilates,<br>and<br>movement<br>learning with<br>depth.</h1>
      <p class="body" style="margin-top:8px;width:190px">Classes and educational formats for people who want strength, nuance, confidence, and a more intelligent relationship with their bodies.</p>
      <div class="btn-row"><span class="btn">Explore events</span><span class="btn btn--outline">See about 1:1</span></div>
    </div>
    <div class="photo ph-beach" role="img" aria-label="Group practising yoga together on a beach" style="left:286px;top:31px;width:227px;height:239px"></div>
  </section>

  <section class="band--beige" style="height:159px;padding:27px 0 0 70px">
    <div class="card-grid">
      <div class="info-card" style="height:102px"><p class="eyebrow">Yoga</p><h3>Clear, adaptable practice</h3><p class="body">Movement that respects the body in front of us. Expect thoughtful sequencing, grounded language, and space to notice.</p></div>
      <div class="info-card" style="height:102px"><p class="eyebrow">Pilates</p><h3>Strength with coordination</h3><p class="body">Practical sessions for breath, control, lower spine mobility, and sustainable strength.</p></div>
      <div class="info-card" style="height:102px"><p class="eyebrow">One-to-one</p><h3>Personal movement support</h3><p class="body">Individual sessions for students and teachers who want specific attention, a calmer plan, or support alongside bodywork.</p></div>
    </div>
  </section>

  <section class="band--white" style="height:253px">
    <div style="position:absolute;left:70px;top:70px;width:225px">
      <p class="eyebrow">Studio classes</p>
      <h2 class="title" style="font-size:18px">Join regular practice.</h2>
      <p class="body" style="margin-top:6px">Studio classes are listed through partner spaces. Use the links below as placeholders for current schedules and booking pages.</p>
      <ul class="list-rows" style="margin-top:6px"><li>Weekly yoga classes · external studio link</li><li>Pilates small groups · external studio link</li><li>Private movement sessions · inquiry</li></ul>
    </div>
    <div class="photo ph-sunset" role="img" aria-label="Person standing on a mountain ridge at sunrise" style="left:317px;top:28px;width:188px;height:195px"></div>
  </section>

  <section class="band--beige" style="height:509px;padding:20px 0 0 70px">
    <p class="eyebrow">Workshops, retreats, trainings</p>
    <h2 class="title" style="font-size:17px;margin-bottom:8px">Upcoming movement education.</h2>
    <div class="card-grid" style="grid-auto-rows:206px 192px">
      <article class="event-card"><div class="ph ph-mono" role="img" aria-label="Person folding forward on the floor in black and white"></div><div class="event-body"><p class="event-meta">21–22 September · Antwerp, Belgium</p><h3>Kavenda and Natural Movement Weekend</h3><p class="body">A small-group immersion exploring support, breath, walking, and the felt sense of uprightness.</p><span class="btn btn--outline">Learn more</span></div></article>
      <article class="event-card"><div class="ph ph-mono2" role="img" aria-label="Person in a downward dog on a mat in black and white"></div><div class="event-body"><p class="event-meta">18 October 2025 · Studio guest training</p><h3>Anatomy for Yoga Teachers</h3><p class="body">Practical anatomy and sequencing for teachers who want clearer cueing and more responsive classes.</p><span class="btn btn--outline">Learn more</span></div></article>
      <article class="event-card"><div class="ph ph-sunset" role="img" aria-label="Figure stretching in warm evening light"></div><div class="event-body"><p class="event-meta">6–9 February 2026 · Ardennes, Belgium</p><h3>Winter Retreat: Structure and Ease</h3><p class="body">Movement, rest, hands-on exploration, and quiet study in a relaxed format with generous space.</p><span class="btn btn--outline">Learn more</span></div></article>
      <article class="event-card"><div class="ph ph-studio" role="img" aria-label="Group of women standing in a studio"></div><div class="event-body"><p class="event-meta">Monthly · Ghent and online</p><h3>Pilates Foundations Lab</h3><p class="body">A focused practice lab for breath, strength, coordination, and adaptable movement choices.</p><span class="btn btn--outline">Learn more</span></div></article>
    </div>
  </section>

  <footer class="site-footer" style="height:84px">
    <div><span class="footer-brand">Liesbet Oonwerk</span><p class="body">Movement education with clarity, warmth, and practical anatomy.</p></div>
    <div class="footer-col"><h4>Explore</h4><ul><li>Kavenda</li><li>Events</li><li>Work with me</li></ul></div>
    <div class="footer-col"><h4>Connect</h4><ul><li>About</li><li>Testimonials</li><li>Contact</li></ul></div>
  </footer>

  <!-- ABOUT -->
  <header class="site-nav">
    <div class="brand"><span class="brand-dot"></span>Liesbet Oonwerk</div>
    <nav class="nav-links"><span>KAVENDA</span><span>MOVEMENT</span><span>EVENTS</span><span>WORK WITH ME</span><span>ABOUT</span><span>TESTIMONIALS</span><span>CONTACT</span></nav>
    <span class="nav-book">BOOK A SESSION</span>
  </header>

  <section class="band--white" style="height:247px">
    <div style="position:absolute;left:55px;top:67px;width:220px">
      <p class="eyebrow">About</p>
      <h1 class="display">Meet Liesbet<br>Oonwerk.</h1>
      <p class="body" style="margin-top:8px;width:190px">A Kavenda® Structural Integration practitioner and movement educator with a calm, precise, and deeply human approach to working with bodies.</p>
    </div>
    <div class="photo ph-portrait" role="img" aria-label="Portrait of Liesbet Oonwerk" style="left:286px;top:28px;width:227px;height:195px"></div>
  </section>

  <section class="band--beige" style="height:203px">
    <div style="position:absolute;left:133px;top:31px;width:305px">
      <h2 class="title" style="font-size:17px;margin-bottom:8px">Bio</h2>
      <p class="body">Liesbet works at the intersection of hands-on structural bodywork and movement teaching. Her practice is grounded in the belief that bodies are not problems to be fixed, but living systems that respond to attention, context, support, and intelligent challenge.</p>
      <p class="body" style="margin-top:5px">In Kavenda sessions, she works with fascia, posture, breath, and the body's relationship to gravity. In teaching, she draws from yoga, Pilates, anatomy, somatic inquiry, and the practical realities of people who want to feel more capable in daily life.</p>
      <p class="body" style="margin-top:5px">Her style is warm and direct. She values clear language, careful listening, and playful curiosity without losing precision. Students and clients often describe the work as spacious, clarifying, and practical.</p>
    </div>
  </section>

  <section class="band--white" style="height:125px;padding:20px 0 0 70px">
    <div class="card-grid">
      <div class="info-card" style="height:75px"><p class="eyebrow">Approach</p><h3>Collaborative</h3><p class="body">Sessions are built with the person in the room, not imposed from a formula.</p></div>
      <div class="info-card" style="height:75px"><p class="eyebrow">Language</p><h3>Clear</h3><p class="body">Body knowledge is translated into usable, grounded cues and observations.</p></div>
      <div class="info-card" style="height:75px"><p class="eyebrow">Pace</p><h3>Responsive</h3><p class="body">The work respects nervous systems, history, curiosity, and consent.</p></div>
    </div>
  </section>

  <footer class="site-footer" style="height:98px">
    <div><span class="footer-brand">Liesbet Oonwerk</span><p class="body">A warm, grounded practice for structural integration and movement education.</p></div>
    <div class="footer-col"><h4>Explore</h4><ul><li>Kavenda</li><li>Movement</li><li>Events</li><li>Work with me</li></ul></div>
    <div class="footer-col"><h4>Connect</h4><ul><li>Testimonials</li><li>Contact</li><li>Brand identity</li></ul></div>
  </footer>
</div>

<!-- ================= RIGHT COLUMN ================= -->
<div class="column column--right">

  <!-- KAVENDA -->
  <header class="site-nav">
    <div class="brand"><span class="brand-dot"></span>Liesbet Oonwerk</div>
    <nav class="nav-links"><span>KAVENDA</span><span>MOVEMENT</span><span>EVENTS</span><span>WORK WITH ME</span><span>ABOUT</span><span>TESTIMONIALS</span><span>CONTACT</span></nav>
    <span class="nav-book">BOOK A SESSION</span>
  </header>

  <section class="band--white" style="height:250px">
    <div style="position:absolute;left:63px;top:39px;width:215px">
      <p class="eyebrow">Bodywork</p>
      <h1 class="display">Kavenda®<br>Structural<br>Integration</h1>
      <p class="body" style="margin-top:8px;width:190px">A hands-on process for improving relationship with gravity, posture, breath, coordination, and the felt sense of being at home in your body.</p>
      <div class="btn-row"><span class="btn">Book a session</span><span class="btn btn--outline">Read FAQ</span></div>
    </div>
    <div class="photo ph-hands" role="img" aria-label="Practitioner's hands working on a client's back" style="left:284px;top:28px;width:227px;height:195px"></div>
  </section>

  <section class="band--beige" style="height:156px;padding:31px 0 0 70px">
    <div class="card-grid">
      <div class="info-card" style="height:97px"><p class="eyebrow">What it is</p><h3>Structural bodywork</h3><p class="body">Kavenda works with connective tissue, perception, and movement habits. Sessions combine touch, guided movement, and conversation so change can become useful in daily life.</p></div>
      <div class="info-card" style="height:97px"><p class="eyebrow">Who it helps</p><h3>People with patterns</h3><p class="body">Clients often come for posture, recurring tension, recovery after change or injury, performance support, breath, balance, or a desire to move with more confidence.</p></div>
      <div class="info-card" style="height:97px"><p class="eyebrow">How it feels</p><h3>Specific and collaborative</h3><p class="body">Touch can be deep or subtle, always responsive. You stay involved through feedback, breath, small movements, and noticing what changes.</p></div>
    </div>
  </section>

  <section class="band--white" style="height:206px">
    <div style="position:absolute;left:70px;top:30px;width:200px">
      <p class="eyebrow">Session flow</p>
      <h2 class="title" style="font-size:18px">What happens in a session?</h2>
      <p class="body" style="margin-top:6px">Each appointment begins with a short conversation and simple movement observation. Hands-on work usually takes place on a table, seated, or standing, depending on what is most useful for the session.</p>
      <p class="body" style="margin-top:4px">You leave with practical movement cues or awareness points, not homework for the sake of homework. The aim is integration: changes that make sense when you walk, sit, teach, train, parent, work, or rest.</p>
    </div>
    <div style="position:absolute;left:284px;top:58px;width:225px">
      <h3 style="font-family:Raleway,sans-serif;font-weight:500;font-size:9px;margin-bottom:4px">The classic series</h3>
      <ul class="list-rows"><li>Sessions 1–3: breath, support, outer sleeve, orientation.</li><li>Sessions 4–7: deeper structural relationships through pelvis, spine, head, and feet.</li><li>Sessions 8–10: integration and personal movement patterns.</li></ul>
    </div>
  </section>

  <section class="band--beige" style="height:166px">
    <div style="position:absolute;left:70px;top:31px;width:200px">
      <p class="eyebrow">Pricing</p>
      <h2 class="title" style="font-size:18px">Clear session options.</h2>
      <p class="body" style="margin-top:6px">Exact pricing and location can be adjusted when Liesbet confirms availability.</p>
    </div>
    <div style="position:absolute;left:284px;top:28px;width:220px;background:#fff;padding:8px 9px 10px">
      <div style="display:flex;justify-content:space-between;font-size:4.6px;color:var(--muted);padding:5px 0;border-bottom:1px solid var(--line)"><span>Kavenda session · 75 minutes</span><b style="color:var(--darkgrey);font-size:6px">€95</b></div>
      <div style="display:flex;justify-content:space-between;font-size:4.6px;color:var(--muted);padding:5px 0;border-bottom:1px solid var(--line)"><span>Kaven Movement session · 60 minutes</span><b style="color:var(--darkgrey);font-size:6px">€80</b></div>
      <div style="display:flex;justify-content:space-between;font-size:4.6px;color:var(--muted);padding:5px 0"><span>Intro conversation · 20 minutes</span><b style="color:var(--darkgrey);font-size:6px">Free</b></div>
      <span class="btn" style="margin-top:4px">Book a session</span>
    </div>
  </section>

  <section class="band--white" style="height:159px;padding:26px 0 0 70px">
    <p class="eyebrow">FAQ</p>
    <h2 class="title" style="font-size:17px;margin-bottom:10px">Questions people often ask.</h2>
    <div style="display:grid;grid-template-columns:212px 212px;gap:8px">
      <div style="border:1px solid var(--line);font-size:4.6px;padding:8px 7px;background:#fff">▸ Is Kavenda massage?</div>
      <div style="border:1px solid var(--line);font-size:4.6px;padding:8px 7px;background:#fff">▸ Do I need the ten-series?</div>
      <div style="border:1px solid var(--line);font-size:4.6px;padding:8px 7px;background:#fff">▸ What should I wear?</div>
      <div style="border:1px solid var(--line);font-size:4.6px;padding:8px 7px;background:#fff">▸ Can it support movement practice?</div>
    </div>
  </section>

  <footer class="site-footer" style="height:83px">
    <div><span class="footer-brand">Liesbet Oonwerk</span><p class="body">Kavenda® is a registered service mark of the Kaven Guild.</p></div>
    <div class="footer-col"><h4>Explore</h4><ul><li>Movement</li><li>Events</li><li>Work with me</li></ul></div>
    <div class="footer-col"><h4>Connect</h4><ul><li>About</li><li>Testimonials</li><li>Contact</li></ul></div>
  </footer>

  <!-- EVENTS -->
  <header class="site-nav">
    <div class="brand"><span class="brand-dot"></span>Liesbet Oonwerk</div>
    <nav class="nav-links"><span>KAVENDA</span><span>MOVEMENT</span><span>EVENTS</span><span>WORK WITH ME</span><span>ABOUT</span><span>TESTIMONIALS</span><span>CONTACT</span></nav>
    <span class="nav-book">BOOK A SESSION</span>
  </header>

  <section class="band--white" style="height:144px;padding:39px 0 0 70px">
    <p class="eyebrow">Calendar</p>
    <h1 class="display" style="font-size:29px">Events and education.</h1>
    <p class="body" style="margin-top:8px;width:300px">Trainings, workshops, retreats, and class dates for students, teachers, and curious movers. The cards are generated from one simple data list.</p>
  </section>

  <section class="band--beige" style="height:469px;padding:31px 0 0 70px">
    <div class="card-grid" style="grid-auto-rows:203px 195px">
      <article class="event-card"><div class="ph ph-mono" role="img" aria-label="Person folding forward on the floor in black and white"></div><div class="event-body"><p class="event-meta">21–22 September · Antwerp, Belgium</p><h3>Kavenda and Natural Movement Weekend</h3><p class="body">A small-group immersion exploring support, breath, walking, and the felt sense of uprightness.</p><span class="btn btn--outline">Learn more</span></div></article>
      <article class="event-card"><div class="ph ph-mono2" role="img" aria-label="Person in a downward dog on a mat in black and white"></div><div class="event-body"><p class="event-meta">18 October 2025 · Studio guest training</p><h3>Anatomy for Yoga Teachers</h3><p class="body">Practical anatomy and sequencing for teachers who want clearer cueing and more responsive classes.</p><span class="btn btn--outline">Learn more</span></div></article>
      <article class="event-card"><div class="ph ph-sunset" role="img" aria-label="Figure stretching in warm evening light"></div><div class="event-body"><p class="event-meta">6–9 February 2026 · Ardennes, Belgium</p><h3>Winter Retreat: Structure and Ease</h3><p class="body">Movement, rest, hands-on exploration, and quiet study in a relaxed format with generous space.</p><span class="btn btn--outline">Learn more</span></div></article>
      <article class="event-card"><div class="ph ph-studio" role="img" aria-label="Group of women standing in a studio"></div><div class="event-body"><p class="event-meta">Monthly · Ghent and online</p><h3>Pilates Foundations Lab</h3><p class="body">A focused practice lab for breath, strength, coordination, and adaptable movement choices.</p><span class="btn btn--outline">Learn more</span></div></article>
    </div>
  </section>

  <section class="band--teal" style="height:156px">
    <div style="position:absolute;left:70px;top:30px;width:200px">
      <p class="eyebrow">Host Liesbet</p>
      <h2 class="title title--light" style="font-size:17px">Want a workshop at your studio?</h2>
      <p class="body body--light" style="margin-top:6px">Invite Liesbet for anatomy, sequencing, Kavenda-informed movement, teacher development, or a retreat format tailored to your community.</p>
    </div>
    <div style="position:absolute;left:277px;top:72px;width:227px"><span class="btn btn--wide">Collaboration inquiry</span></div>
  </section>

  <footer class="site-footer" style="height:89px">
    <div><span class="footer-brand">Liesbet Oonwerk</span><p class="body">Events are updated through the shared event data file.</p></div>
    <div class="footer-col"><h4>Explore</h4><ul><li>Kavenda</li><li>Movement</li><li>Work with me</li></ul></div>
    <div class="footer-col"><h4>Connect</h4><ul><li>About</li><li>Testimonials</li><li>Contact</li></ul></div>
  </footer>

  <!-- WORK WITH ME -->
  <header class="site-nav">
    <div class="brand"><span class="brand-dot"></span>Liesbet Oonwerk</div>
    <nav class="nav-links"><span>KAVENDA</span><span>MOVEMENT</span><span>EVENTS</span><span>WORK WITH ME</span><span>ABOUT</span><span>TESTIMONIALS</span><span>CONTACT</span></nav>
    <span class="nav-book">BOOK A SESSION</span>
  </header>

  <section class="band--white" style="height:278px">
    <div style="position:absolute;left:63px;top:28px;width:215px">
      <p class="eyebrow">For studios and organisations</p>
      <h1 class="display">Guest<br>teaching,<br>workshops,<br>and teacher<br>development.</h1>
      <p class="body" style="margin-top:8px;width:200px">Bring Liesbet in for grounded education that helps students and teachers understand bodies with more clarity, care, and practical skill.</p>
      <div class="btn-row"><span class="btn">Start an inquiry</span></div>
    </div>
    <div class="photo ph-sunset" role="img" aria-label="Person on a hilltop in golden morning light" style="left:284px;top:23px;width:227px;height:231px"></div>
  </section>

  <section class="band--beige" style="height:144px;padding:23px 0 0 70px">
    <div class="card-grid">
      <div class="info-card" style="height:94px"><p class="eyebrow">Guest teaching</p><h3>Classes and intensives</h3><p class="body">Accessible, intelligent movement sessions for studio communities, retreats, and training programs.</p></div>
      <div class="info-card" style="height:94px"><p class="eyebrow">Anatomy &amp; sequencing</p><h3>Useful body knowledge</h3><p class="body">Teaching that translates anatomy into cueing, class design, and sharper observation.</p></div>
      <div class="info-card" style="height:94px"><p class="eyebrow">Teacher development</p><h3>Continuing education</h3><p class="body">Support for teachers who want less formula, more discernment, and more confidence in the room.</p></div>
    </div>
  </section>

  <section class="band--white" style="height:291px">
    <div style="position:absolute;left:70px;top:100px;width:190px">
      <p class="eyebrow">Collaboration inquiry</p>
      <h2 class="title" style="font-size:18px">Tell Liesbet what you are imagining.</h2>
      <p class="body" style="margin-top:6px">Share the format, audience, location, timing, and the kind of learning you want to create. This form opens an email draft so the message stays personal and editable.</p>
    </div>
    <div class="form-card" style="left:273px;top:28px;width:230px;height:242px">
      <div class="field"><label>Name</label><div class="input"></div></div>
      <div class="field"><label>Studio or organisation</label><div class="input"></div></div>
      <div class="field"><label>Format</label><div class="input input--select"><span>Guest teaching</span><span>⌄</span></div></div>
      <div class="field"><label>Message</label><div class="input input--area"></div></div>
      <span class="btn btn--teal btn--wide">Send inquiry</span>
    </div>
  </section>

  <footer class="site-footer" style="height:84px">
    <div><span class="footer-brand">Liesbet Oonwerk</span><p class="body">Education for studios, organisations, teachers, and retreat communities.</p></div>
    <div class="footer-col"><h4>Explore</h4><ul><li>Kavenda</li><li>Movement</li><li>Events</li></ul></div>
    <div class="footer-col"><h4>Connect</h4><ul><li>About</li><li>Testimonials</li><li>Contact</li></ul></div>
  </footer>

  <!-- TESTIMONIALS -->
  <header class="site-nav">
    <div class="brand"><span class="brand-dot"></span>Liesbet Oonwerk</div>
    <nav class="nav-links"><span>KAVENDA</span><span>MOVEMENT</span><span>EVENTS</span><span>WORK WITH ME</span><span>ABOUT</span><span>TESTIMONIALS</span><span>CONTACT</span></nav>
    <span class="nav-book">BOOK A SESSION</span>
  </header>

  <section class="band--white" style="height:173px;padding:59px 0 0 70px">
    <p class="eyebrow">Testimonials</p>
    <h1 class="display" style="font-size:29px;line-height:31px">Words from clients,<br>students, and trainees.</h1>
    <p class="body" style="margin-top:8px;width:260px">A mix of bodywork, class, training, and collaboration feedback. Replace these with approved real testimonials before launch.</p>
  </section>

  <section class="band--beige" style="height:195px;padding:27px 0 0 70px">
    <div style="display:grid;grid-template-columns:209px 209px;gap:8px">
      <div class="info-card" style="height:68px"><h3>Client</h3><p class="body">“After three sessions I felt more space in my breathing and less effort in standing. Liesbet explains just enough, then lets the body learn.”</p></div>
      <div class="info-card" style="height:68px"><h3>Yoga student</h3><p class="body">“Her classes are intelligent without being complicated. I always leave with one clear thing I can use in my own practice.”</p></div>
      <div class="info-card" style="height:68px"><h3>Teacher trainee</h3><p class="body">“The anatomy module changed how I cue. It became less about perfect shapes and more about what students actually need.”</p></div>
      <div class="info-card" style="height:68px"><h3>Studio host</h3><p class="body">“Liesbet brought warmth, precision, and a beautiful sense of curiosity to our teacher development weekend.”</p></div>
    </div>
  </section>

  <section class="band--teal" style="height:144px">
    <div style="position:absolute;left:70px;top:31px;width:200px">
      <p class="eyebrow">Begin</p>
      <h2 class="title title--light" style="font-size:17px">Start with a session or a conversation.</h2>
      <p class="body body--light" style="margin-top:6px">Book Kavenda, ask about movement support, or invite Liesbet to teach.</p>
    </div>
    <div style="position:absolute;left:277px;top:64px;width:227px"><span class="btn btn--wide">Book a session</span></div>
  </section>

  <footer class="site-footer" style="height:94px">
    <div><span class="footer-brand">Liesbet Oonwerk</span><p class="body">Testimonials for bodywork, movement classes, trainings, and studio collaborations.</p></div>
    <div class="footer-col"><h4>Explore</h4><ul><li>Kavenda</li><li>Movement</li><li>Events</li></ul></div>
    <div class="footer-col"><h4>Connect</h4><ul><li>About</li><li>Contact</li><li>Brand identity</li></ul></div>
  </footer>

  <!-- CONTACT -->
  <header class="site-nav">
    <div class="brand"><span class="brand-dot"></span>Liesbet Oonwerk</div>
    <nav class="nav-links"><span>KAVENDA</span><span>MOVEMENT</span><span>EVENTS</span><span>WORK WITH ME</span><span>ABOUT</span><span>TESTIMONIALS</span><span>CONTACT</span></nav>
    <span class="nav-book">BOOK A SESSION</span>
  </header>

  <section class="band--white" style="height:250px">
    <div style="position:absolute;left:63px;top:31px;width:215px">
      <p class="eyebrow">Contact</p>
      <h1 class="display">Book a<br>session or<br>start a<br>conversation.</h1>
      <p class="body" style="margin-top:8px;width:195px">Use the form for Kavenda, Kaven Movement, one-to-one movement support, workshops, trainings, retreats, or general questions.</p>
    </div>
    <div class="photo ph-hands" role="img" aria-label="Practitioner's hands working on a client's back" style="left:284px;top:23px;width:227px;height:191px"></div>
  </section>

  <section class="band--beige" style="height:281px">
    <div style="position:absolute;left:70px;top:60px;width:190px">
      <p class="eyebrow">Booking</p>
      <h2 class="title" style="font-size:18px">Tell Liesbet what you need.</h2>
      <p class="body" style="margin-top:6px">The form opens an email draft with your details. For a live site, this can be connected to a booking tool, form service, or CMS form service.</p>
      <p class="body" style="margin-top:6px">Email: hello@liesbetoonwerk.be</p>
      <p class="body" style="margin-top:6px">Sessions: Kavenda, Kaven Movement, private movement</p>
      <p class="body" style="margin-top:6px">Education: guest teaching, workshops, trainings, retreats</p>
    </div>
    <div class="form-card" style="left:273px;top:23px;width:230px;height:219px">
      <div class="field"><label>Name</label><div class="input"></div></div>
      <div class="field"><label>Email</label><div class="input"></div></div>
      <div class="field"><label>I am interested in</label><div class="input input--select"><span>Kavenda® Structural Integration</span><span>⌄</span></div></div>
      <div class="field"><label>Message</label><div class="input input--area" style="height:40px">A little context, availability, or what you are curious about.</div></div>
      <span class="btn btn--teal btn--wide">Send booking request</span>
    </div>
  </section>

  <footer class="site-footer" style="height:95px">
    <div><span class="footer-brand">Liesbet Oonwerk</span><p class="body">Contact Liesbet for sessions, teaching, workshops, trainings, and retreats.</p></div>
    <div class="footer-col"><h4>Explore</h4><ul><li>Kavenda</li><li>Movement</li><li>Events</li><li>Work with me</li></ul></div>
    <div class="footer-col"><h4>Connect</h4><ul><li>About</li><li>Testimonials</li><li>Brand identity</li></ul></div>
  </footer>
</div>

</body>
</html>
```